Plakat-Design für Verkauf von Bio-zertifiziertem Saatgut
Zielgruppe
Wir sind ein Start Up und verkaufen BIO Zertifiziertes Saatgut für Gemüse, Kräuter, Heilpflanzen und essbare Sprossen etc. Zielgruppe ist vor allem die DIY Community von Jung bis Alt.
Aufgabenstellung
*** INFO*** Da es keine 'Kalender'-Projekte gibt, sollten wir das Projekt unter 'Plakat' einstellen ***INFO***
Wir sind auf der Suche nach einem Design für einen Monatskalender (Deckblatt, 12 Monate, Schlussblatt) der als ewiger Aussaatkalender fungieren soll (Keine Jahreszahlen, nur der Monat). Jeden Monat sollen die Sorten gezeigt werden die jetzt ausgesät werden können. Am Besten teilweise (nicht alle) als Illustrationen oder Bilder. Die Sorten orientieren sich an unserem Saatgutsortiment. Als Unterteilung kann man: 'Vorzucht im Haus', Frühbeet' und 'Direktsaat'
Die Informationen welche Samen wann ausgesät werden, kommen von uns. (Erstmal Platzhalter für das Design nutzen) Falls der Designer Erfahrung in diesem Bereich hat, kann er die Informationen auch selber einfügen. Sonst ist der Designer für Layout und Illustrationen/Bilder zuständig. Toll wäre wenn für jeden Monat noch eine 'Bauernweisheit' zum Thema Pflanzen / Aussaat / Garten hinzugefügt werden kann.
Das Design soll sich an unserer CI der Website www.keimfeld.de orientieren. Logo, Farben und Fonts (My-Everything, BW Mitga) sind im Anhang beigefügt. Auch die Vorlage der Druckerei ist beigefügt. Format: DIN A4 hoch (210 x 297 mm), beidseitig bedruckt so das man den Kalender auch Aufgeklappt nutzen kann.
Falls noch Informationen benötigt werden, dann meldet euch gerne!

```html
<!DOCTYPE html>
<html lang="de">
<head>
<meta charset="utf-8">
<title>Keimfeld – Aussaatkalender</title>
<link href="https://fonts.googleapis.com/css2?family=Allura&family=Mulish:wght@400;600;800&display=swap" rel="stylesheet">
<style>
  :root{
    --backdrop:#a4b4b8;
    --green:#6a8a3c;
    --green-dark:#55722c;
    --text:#4a4a42;
    --paper:#ebe7df;
    --col-sage:#d7dcc8;
    --col-light:#e8eae3;
    --row:#c9d1b5;
    --arch:#c3cbad;
    --panel:rgba(236,233,230,.86);
  }
  *{box-sizing:border-box;margin:0;padding:0}
  html,body{width:1200px;height:882px;overflow:hidden}
  body{background:var(--backdrop);font-family:"Mulish",sans-serif;color:var(--text);position:relative}
  .page{position:absolute;top:181px;width:368px;height:520px;overflow:hidden;box-shadow:0 4px 14px rgba(0,0,0,.18)}
  .cover{left:24px}
  .month-photo{left:416px;background:var(--paper)}
  .month-sowing{left:808px;background:var(--col-light)}

  /* cover */
  .cover-photo{position:absolute;inset:0;background:
    radial-gradient(ellipse at 50% 50%,#5b4a3c 0 30%,transparent 55%),
    linear-gradient(135deg,#3f7a2c 0%,#c8472b 30%,#4f8a32 50%,#d9a23a 70%,#3d6e2a 100%)}
  .cover-panel{position:absolute;left:104px;top:175px;width:206px;height:245px;border-radius:18px;background:var(--panel);text-align:center;padding-top:16px}
  .brand{display:flex;align-items:center;justify-content:center;gap:6px;font-weight:600;font-size:13px;letter-spacing:2px;color:var(--green)}
  .brand-dot{width:9px;height:9px;border-radius:50%;background:var(--green)}
  .cover-title{margin-top:40px;font-weight:800;font-size:27px;line-height:32px;color:var(--green);letter-spacing:.5px}
  .cover-rule{margin:6px auto 0;width:184px;height:1.5px;background:var(--green)}
  .cover-sub{margin-top:12px;font-size:11px;line-height:16px;color:var(--text)}

  /* month photo page */
  .script{font-family:"Allura",cursive;color:var(--green);line-height:1}
  .month-photo .script{position:absolute;left:34px;top:22px;font-size:104px}
  .seedling-photo{position:absolute;left:0;top:128px;width:100%;height:392px;background:linear-gradient(180deg,#6a5a4c 0%,#4b3f34 35%,#7a7065 65%,#9c948a 100%)}
  .info-box{position:absolute;left:0;top:326px;width:354px;height:98px;background:rgba(236,232,226,.9);border-radius:0 14px 14px 0;padding:12px 10px 0 22px}
  .info-box h2{font-size:9.5px;font-weight:800;color:var(--green-dark);letter-spacing:.3px}
  .info-box p{margin-top:8px;font-size:7px;line-height:8.6px;color:#5a5650}

  /* month sowing page */
  .col{position:absolute;top:0;height:424px}
  .col-direct{left:0;width:121px;background:var(--col-sage)}
  .col-frame{left:121px;width:121px;background:var(--col-light)}
  .col-indoor{left:242px;width:126px;background:var(--col-sage)}
  .group{position:absolute;width:68px;text-align:center}
  .group h3{font-size:10.5px;font-weight:800;color:var(--green);line-height:12px;letter-spacing:.3px;margin-bottom:4px}
  .arch{height:33px;background:var(--arch);border-radius:34px 34px 0 0;display:flex;align-items:center;justify-content:center}
  .arch svg{width:24px;height:20px;stroke:var(--green);fill:none;stroke-width:1.2}
  .sorts{list-style:none}
  .sorts li{height:13px;margin-top:1.2px;background:var(--row);text-align:left;padding-left:6px;font-size:7.6px;line-height:13px;color:#3f3f38}
  .g-direct{left:25px;top:84px}
  .g-frame{left:148px;top:130px}
  .g-indoor{left:272px;top:252px}
  .broccoli-art{position:absolute;left:222px;top:40px;width:140px;height:170px;border-radius:45% 50% 40% 55%;background:radial-gradient(circle at 35% 35%,#4f7a3a 0 38%,transparent 60%),radial-gradient(circle at 75% 70%,#8c6a92 0 22%,#dcd7c8 40%,transparent 62%)}
  .zucchini-art{position:absolute;left:72px;top:308px;width:188px;height:108px;border-radius:50% 60% 40% 50%;background:radial-gradient(ellipse at 30% 70%,#3f6a3a 0 35%,transparent 55%),radial-gradient(ellipse at 75% 35%,#d7c27a 0 30%,transparent 55%)}
  .footer-band{position:absolute;left:0;top:424px;width:100%;height:96px;background:var(--paper)}
  .footer-band .script{position:absolute;left:26px;top:12px;font-size:62px}
  .footer-word{position:absolute;left:62px;top:54px;font-weight:800;font-size:14px;color:#5b6a2e}
  .seeds-art{position:absolute;left:160px;top:24px;width:150px;height:60px;border-radius:40%;background:radial-gradient(ellipse at 60% 60%,#9a7a52 0 20%,rgba(154,122,82,.3) 45%,transparent 70%)}
  .footer-brand{position:absolute;right:16px;top:60px;font-size:9px;font-weight:600;color:var(--green);letter-spacing:1px}
</style>
</head>
<body>

<section class="page cover">
  <div class="cover-photo" role="img" aria-label="Foto: frisches Gemüse und Kräuter rund um eine Holzfläche"></div>
  <div class="cover-panel">
    <div class="brand"><span class="brand-dot"></span>KEIMFELD</div>
    <h1 class="cover-title">AUSSAAT-<br>KALENDER</h1>
    <div class="cover-rule"></div>
    <p class="cover-sub">Saisonkalender<br>für Gemüse und Kräuter</p>
  </div>
</section>

<section class="page month-photo">
  <div class="script">April</div>
  <div class="seedling-photo" role="img" aria-label="Foto: Keimlinge in Tontöpfen und Samen auf Holz"></div>
  <div class="info-box">
    <h2>UDANIS CUPTA DOLUT REM ET</h2>
    <p>Equamus sitatust, num as sim consedio. Et pore niscipi ciisquiae earum facearum cumeni ipsunt officiat fugitation etust, tection rem ut latur, corepellatem as et alit ex eveliquos as sunte omnis molutemo beat eostioribus, con nonectiorum, explita sumquos alignit perchitat reped exernat quam accus quatures il endelibus, conet litatur?</p>
  </div>
</section>

<section class="page month-sowing">
  <div class="col col-direct"></div>
  <div class="col col-frame"></div>
  <div class="col col-indoor"></div>

  <div class="broccoli-art" role="img" aria-label="Illustration: Brokkoli und Rübchen"></div>
  <div class="zucchini-art" role="img" aria-label="Illustration: Zucchini mit Blüte"></div>

  <div class="group g-direct">
    <h3>DIREKTSAAT</h3>
    <div class="arch"><svg viewBox="0 0 24 20"><path d="M4 6h9l4-3M8 12a2 2 0 1 0 4 0M10 16v2"/></svg></div>
    <ul class="sorts">
      <li>Radieschen</li><li>Aubergine</li><li>Gurke</li><li>Kopfsalat</li><li>Blumenkohl</li><li>Brokkoli</li><li>Bohnen</li><li>Radieschen</li><li>Gurke</li><li>Spitzkohl</li><li>Aubergine</li><li>Bohnen</li><li>Radieschen</li>
    </ul>
  </div>

  <div class="group g-frame">
    <h3>FRÜHBEET</h3>
    <div class="arch"><svg viewBox="0 0 24 20"><path d="M3 8l9-4 9 4-9 4zM3 8v7l9 4 9-4V8M12 12v7"/></svg></div>
    <ul class="sorts">
      <li>Radieschen</li><li>Aubergine</li><li>Gurke</li><li>Kopfsalat</li><li>Blumenkohl</li><li>Brokkoli</li><li>Bohnen</li><li>Aubergine</li><li>Blumenkohl</li>
    </ul>
  </div>

  <div class="group g-indoor">
    <h3>VORZUCHT<br>IM HAUS</h3>
    <div class="arch"><svg viewBox="0 0 24 20"><path d="M3 9l9-6 9 6v10H3zM12 18v-6M12 13c-3 0-4-2-4-4 3 0 4 2 4 4zM12 13c3 0 4-2 4-4-3 0-4 2-4 4"/></svg></div>
    <ul class="sorts">
      <li>Radieschen</li><li>Aubergine</li><li>Gurke</li><li>Kopfsalat</li><li>Blumenkohl</li><li>Brokkoli</li>
    </ul>
  </div>

  <div class="footer-band">
    <div class="script">April</div>
    <div class="footer-word">Aussaat</div>
    <div class="seeds-art" role="img" aria-label="Illustration: verstreute Samenkörner"></div>
    <div class="footer-brand">KEIMFELD</div>
  </div>
</section>

</body>
</html>
```